Restaurant Digital TV Menu Pictures

Need a digital menu board, image square of food. Something simple for customer to look and point to or say the food number. Image square 4x6, 5x7 or various of that. Vietnamese restaurant type food. I need template created and designer choice of design. Color scheme orange and white and little green. I would like to in the title of the food myself and written detail myself. I just need the template and possible have the design edit the picture a bit. Total food about 30 image will mostly be about 20-30 images. This will be display on a TV screen 16:9 size on a 55 inch tv. Attached is the food menu item. Also attach how the image off food will be taken. Also attach of other people design on the web. However, I would like number be label on the food item. I can find tune the correct information and food type and numbers later.

Font styles to use
Decorative

Colors
f37122
fffefb
9bcb3c

Requirements
Must have
• Photo edit food image basic making it pop. Make it look better, not magic, but better than my photography. Asian feel to the design.
Nice to have
• Fresh image of ingredients, (cilantro, freshly cook, non fast food) Image of green food

```html
<!DOCTYPE html>
<html lang="en">
<head>
<meta charset="utf-8">
<title>Menu Board</title>
<link rel="stylesheet" href="https://fonts.googleapis.com/css2?family=Bungee&display=swap">
<style>
  :root {
    --orange: #f37122;
    --orange-light: #f8a23a;
    --rust: #b8460e;
    --cream: #fffefb;
    --green: #17882a;
    --leaf: #9bcb3c;
    --stage: #ffffff;
  }
  * { box-sizing: border-box; margin: 0; padding: 0; }
  html, body { width: 1200px; height: 786px; overflow: hidden; background: var(--stage); }
  .board {
    position: absolute; left: 0; top: 55px;
    width: 1200px; height: 675px;
    background: radial-gradient(ellipse at center, var(--orange-light) 0%, var(--orange) 80%);
    font-family: "Bungee", system-ui, sans-serif;
  }
  .menu-grid {
    position: absolute; left: 12px; top: 14px;
    display: grid;
    grid-template-columns: repeat(5, 193px);
    grid-template-rows: repeat(4, 152px);
    column-gap: 12px; row-gap: 14px;
  }
  .dish {
    position: relative;
    background: var(--cream);
    border: 2px solid var(--green);
    outline: 2px solid var(--cream);
    overflow: hidden;
  }
  .dish-title {
    position: absolute; left: 3px; right: 3px; top: 3px; height: 31px;
    border: 2px solid var(--green);
    background: var(--cream);
    color: var(--rust);
    font-size: 19px; line-height: 27px; text-align: center;
    z-index: 2;
  }
  .dish-photo {
    position: absolute; left: 56px; right: 0; top: 36px; bottom: 0;
    border-radius: 60px 0 0 60px;
  }
  .dish-photo.beef { background: radial-gradient(circle at 60% 55%, #6b4a32 0%, #7a5c40 35%, #2a2a2a 70%, #e9e6e2 72%); }
  .dish-photo.popcorn { background: radial-gradient(circle at 60% 55%, #c0813e 0%, #b8742f 40%, #eeeae6 65%, #f7f5f2 100%); }
  .dish-desc {
    position: absolute; left: 4px; top: 43px; width: 56px;
    font-size: 3.6px; line-height: 6.2px; color: var(--green);
    z-index: 2;
  }
  .dish-price {
    position: absolute; left: 5px; bottom: 4px;
    font-size: 22px; line-height: 1; color: var(--orange);
    z-index: 2;
  }
  .side-panel {
    position: absolute; left: 1034px; top: 14px;
    width: 158px; height: 649px;
    border: 2px solid var(--green);
    background: var(--cream);
    padding: 3px;
  }
  .side-panel-title {
    background: var(--rust); color: var(--cream);
    font-size: 19px; line-height: 40px; text-align: center;
  }
</style>
</head>
<body>
<main class="board">
  <section class="menu-grid">
    <article class="dish"><h2 class="dish-title">Beef Rice</h2><p class="dish-desc">Lorem ipsum dolor sit amet, consectetur adipiscing elit, sed do eiusmod tempor incididunt ut labore et dolore magna aliqua. Ut enim ad minim veniam, quis nostrud exercitation ullamco laboris nisi ut aliquip ex ea commodo</p><div class="dish-photo beef" role="img" aria-label="Beef rice bowl with spring roll and slaw"></div><p class="dish-price">$9.99</p></article>
    <article class="dish"><h2 class="dish-title">Pop Corn</h2><p class="dish-desc">Lorem ipsum dolor sit amet, consectetur adipiscing elit, sed do eiusmod tempor incididunt ut labore et dolore magna aliqua. Ut enim ad minim veniam, quis nostrud exercitation ullamco laboris nisi ut aliquip ex ea commodo</p><div class="dish-photo popcorn" role="img" aria-label="Popcorn chicken bowl with cilantro"></div><p class="dish-price">$6.99</p></article>
    <article class="dish"><h2 class="dish-title">Beef Rice</h2><p class="dish-desc">Lorem ipsum dolor sit amet, consectetur adipiscing elit, sed do eiusmod tempor incididunt ut labore et dolore magna aliqua. Ut enim ad minim veniam, quis nostrud exercitation ullamco laboris nisi ut aliquip ex ea commodo</p><div class="dish-photo beef" role="img" aria-label="Beef rice bowl with spring roll and slaw"></div><p class="dish-price">$9.99</p></article>
    <article class="dish"><h2 class="dish-title">Pop Corn</h2><p class="dish-desc">Lorem ipsum dolor sit amet, consectetur adipiscing elit, sed do eiusmod tempor incididunt ut labore et dolore magna aliqua. Ut enim ad minim veniam, quis nostrud exercitation ullamco laboris nisi ut aliquip ex ea commodo</p><div class="dish-photo popcorn" role="img" aria-label="Popcorn chicken bowl with cilantro"></div><p class="dish-price">$6.99</p></article>
    <article class="dish"><h2 class="dish-title">Beef Rice</h2><p class="dish-desc">Lorem ipsum dolor sit amet, consectetur adipiscing elit, sed do eiusmod tempor incididunt ut labore et dolore magna aliqua. Ut enim ad minim veniam, quis nostrud exercitation ullamco laboris nisi ut aliquip ex ea commodo</p><div class="dish-photo beef" role="img" aria-label="Beef rice bowl with spring roll and slaw"></div><p class="dish-price">$9.99</p></article>

    <article class="dish"><h2 class="dish-title">Beef Rice</h2><p class="dish-desc">Lorem ipsum dolor sit amet, consectetur adipiscing elit, sed do eiusmod tempor incididunt ut labore et dolore magna aliqua. Ut enim ad minim veniam, quis nostrud exercitation ullamco laboris nisi ut aliquip ex ea commodo</p><div class="dish-photo beef" role="img" aria-label="Beef rice bowl with spring roll and slaw"></div><p class="dish-price">$9.99</p></article>
    <article class="dish"><h2 class="dish-title">Pop Corn</h2><p class="dish-desc">Lorem ipsum dolor sit amet, consectetur adipiscing elit, sed do eiusmod tempor incididunt ut labore et dolore magna aliqua. Ut enim ad minim veniam, quis nostrud exercitation ullamco laboris nisi ut aliquip ex ea commodo</p><div class="dish-photo popcorn" role="img" aria-label="Popcorn chicken bowl with cilantro"></div><p class="dish-price">$6.99</p></article>
    <article class="dish"><h2 class="dish-title">Beef Rice</h2><p class="dish-desc">Lorem ipsum dolor sit amet, consectetur adipiscing elit, sed do eiusmod tempor incididunt ut labore et dolore magna aliqua. Ut enim ad minim veniam, quis nostrud exercitation ullamco laboris nisi ut aliquip ex ea commodo</p><div class="dish-photo beef" role="img" aria-label="Beef rice bowl with spring roll and slaw"></div><p class="dish-price">$9.99</p></article>
    <article class="dish"><h2 class="dish-title">Pop Corn</h2><p class="dish-desc">Lorem ipsum dolor sit amet, consectetur adipiscing elit, sed do eiusmod tempor incididunt ut labore et dolore magna aliqua. Ut enim ad minim veniam, quis nostrud exercitation ullamco laboris nisi ut aliquip ex ea commodo</p><div class="dish-photo popcorn" role="img" aria-label="Popcorn chicken bowl with cilantro"></div><p class="dish-price">$6.99</p></article>
    <article class="dish"><h2 class="dish-title">Beef Rice</h2><p class="dish-desc">Lorem ipsum dolor sit amet, consectetur adipiscing elit, sed do eiusmod tempor incididunt ut labore et dolore magna aliqua. Ut enim ad minim veniam, quis nostrud exercitation ullamco laboris nisi ut aliquip ex ea commodo</p><div class="dish-photo beef" role="img" aria-label="Beef rice bowl with spring roll and slaw"></div><p class="dish-price">$9.99</p></article>

    <article class="dish"><h2 class="dish-title">Beef Rice</h2><p class="dish-desc">Lorem ipsum dolor sit amet, consectetur adipiscing elit, sed do eiusmod tempor incididunt ut labore et dolore magna aliqua. Ut enim ad minim veniam, quis nostrud exercitation ullamco laboris nisi ut aliquip ex ea commodo</p><div class="dish-photo beef" role="img" aria-label="Beef rice bowl with spring roll and slaw"></div><p class="dish-price">$9.99</p></article>
    <article class="dish"><h2 class="dish-title">Pop Corn</h2><p class="dish-desc">Lorem ipsum dolor sit amet, consectetur adipiscing elit, sed do eiusmod tempor incididunt ut labore et dolore magna aliqua. Ut enim ad minim veniam, quis nostrud exercitation ullamco laboris nisi ut aliquip ex ea commodo</p><div class="dish-photo popcorn" role="img" aria-label="Popcorn chicken bowl with cilantro"></div><p class="dish-price">$6.99</p></article>
    <article class="dish"><h2 class="dish-title">Beef Rice</h2><p class="dish-desc">Lorem ipsum dolor sit amet, consectetur adipiscing elit, sed do eiusmod tempor incididunt ut labore et dolore magna aliqua. Ut enim ad minim veniam, quis nostrud exercitation ullamco laboris nisi ut aliquip ex ea commodo</p><div class="dish-photo beef" role="img" aria-label="Beef rice bowl with spring roll and slaw"></div><p class="dish-price">$9.99</p></article>
    <article class="dish"><h2 class="dish-title">Pop Corn</h2><p class="dish-desc">Lorem ipsum dolor sit amet, consectetur adipiscing elit, sed do eiusmod tempor incididunt ut labore et dolore magna aliqua. Ut enim ad minim veniam, quis nostrud exercitation ullamco laboris nisi ut aliquip ex ea commodo</p><div class="dish-photo popcorn" role="img" aria-label="Popcorn chicken bowl with cilantro"></div><p class="dish-price">$6.99</p></article>
    <article class="dish"><h2 class="dish-title">Beef Rice</h2><p class="dish-desc">Lorem ipsum dolor sit amet, consectetur adipiscing elit, sed do eiusmod tempor incididunt ut labore et dolore magna aliqua. Ut enim ad minim veniam, quis nostrud exercitation ullamco laboris nisi ut aliquip ex ea commodo</p><div class="dish-photo beef" role="img" aria-label="Beef rice bowl with spring roll and slaw"></div><p class="dish-price">$9.99</p></article>

    <article class="dish"><h2 class="dish-title">Beef Rice</h2><p class="dish-desc">Lorem ipsum dolor sit amet, consectetur adipiscing elit, sed do eiusmod tempor incididunt ut labore et dolore magna aliqua. Ut enim ad minim veniam, quis nostrud exercitation ullamco laboris nisi ut aliquip ex ea commodo</p><div class="dish-photo beef" role="img" aria-label="Beef rice bowl with spring roll and slaw"></div><p class="dish-price">$9.99</p></article>
    <article class="dish"><h2 class="dish-title">Pop Corn</h2><p class="dish-desc">Lorem ipsum dolor sit amet, consectetur adipiscing elit, sed do eiusmod tempor incididunt ut labore et dolore magna aliqua. Ut enim ad minim veniam, quis nostrud exercitation ullamco laboris nisi ut aliquip ex ea commodo</p><div class="dish-photo popcorn" role="img" aria-label="Popcorn chicken bowl with cilantro"></div><p class="dish-price">$6.99</p></article>
    <article class="dish"><h2 class="dish-title">Beef Rice</h2><p class="dish-desc">Lorem ipsum dolor sit amet, consectetur adipiscing elit, sed do eiusmod tempor incididunt ut labore et dolore magna aliqua. Ut enim ad minim veniam, quis nostrud exercitation ullamco laboris nisi ut aliquip ex ea commodo</p><div class="dish-photo beef" role="img" aria-label="Beef rice bowl with spring roll and slaw"></div><p class="dish-price">$9.99</p></article>
    <article class="dish"><h2 class="dish-title">Pop Corn</h2><p class="dish-desc">Lorem ipsum dolor sit amet, consectetur adipiscing elit, sed do eiusmod tempor incididunt ut labore et dolore magna aliqua. Ut enim ad minim veniam, quis nostrud exercitation ullamco laboris nisi ut aliquip ex ea commodo</p><div class="dish-photo popcorn" role="img" aria-label="Popcorn chicken bowl with cilantro"></div><p class="dish-price">$6.99</p></article>
    <article class="dish"><h2 class="dish-title">Beef Rice</h2><p class="dish-desc">Lorem ipsum dolor sit amet, consectetur adipiscing elit, sed do eiusmod tempor incididunt ut labore et dolore magna aliqua. Ut enim ad minim veniam, quis nostrud exercitation ullamco laboris nisi ut aliquip ex ea commodo</p><div class="dish-photo beef" role="img" aria-label="Beef rice bowl with spring roll and slaw"></div><p class="dish-price">$9.99</p></article>
  </section>

  <aside class="side-panel">
    <h2 class="side-panel-title">Side Panel</h2>
  </aside>
</main>
</body>
</html>
```